ARC VOLLEY Business Card Project

I'd like to request a business card design for the new company I've launched.
The name of the company is "ARC VOLLEY" an indoor unmanned tennis practice facility.
We would like to see designs that use our brand identity color in the logo I've attached.
We hope to get the design with modern, luxurious and elegant tone and manner.
We hope the logo should not be too big.

Business card must have elements as below:
- Logo (One of the logos I've attached)
- Name (In Korean Text) : 박 서 윤
- Title (In Korean Text) : 대표
- Phone Number : 010-8472-3916
- Email Address : seoyun.park@arcvolley-example.co.kr
- Website : www.arcvolley-example.co.kr
- Instagram : arcvolley
- Address (In Korean text) : 경기도 용인시 수지구 풍덕천로 456 미래타워 5층 501호, 502호

Target Market(s)

Tennis amateurs in 20 to 40s

Industry/Entity Type

Sports, Hobby

Contact Information for Business Card

- Logo (One of the logos I've attached) - Name (In Korean Text) : 박 서 윤 - Title (In Korean Text) : 대표 - Phone Number : 010-8472-3916 - Email Address : seoyun.park@arcvolley-example.co.kr - Website : www.arcvolley-example.co.kr - Instagram : arcvolley - Address (In Korean text) : 경기도 용인시 수지구 풍덕천로 456 미래타워 5층 501호, 502호

Font styles to use
Sans Serif

Requirements
Must have
• Double sided
Nice to have
• Logo with intaglio or relief embossing
Should not have
• Logo should not be too big.

```html
<!DOCTYPE html>
<html lang="ko">
<head>
<meta charset="utf-8">
<title>ARC VOLLEY Business Card</title>
<link rel="stylesheet" href="https://fonts.googleapis.com/css2?family=Lato:wght@400;700&family=Noto+Sans+KR:wght@400;700&display=swap">
<style>
  :root {
    --brand-green: #2f5138;
    --brand-grey: #505050;
    --card-white: #ffffff;
    --backdrop: #dcdcd8;
    --text-light: #ffffff;
    --text-dark: #333333;
  }
  * { box-sizing: border-box; margin: 0; padding: 0; }
  html, body {
    width: 1200px; height: 801px; overflow: hidden;
    background: var(--backdrop);
    font-family: "Lato", "Noto Sans KR", sans-serif;
  }
  .sheet {
    position: relative; width: 1200px; height: 801px;
    display: flex; align-items: center; justify-content: center; gap: 40px;
  }
  .card {
    position: relative; width: 540px; height: 300px;
    border-radius: 16px; overflow: hidden;
    box-shadow: 0 10px 24px rgba(0,0,0,.18);
  }
  .card--front { background: var(--card-white); }
  .card--back { background: var(--brand-green); }
  .card-art { position: absolute; inset: 0; width: 100%; height: 100%; }

  .brand { position: absolute; display: flex; align-items: center; }
  .brand-dot { border-radius: 50%; flex: none; }
  .brand-name {
    font-family: "Lato", sans-serif; font-weight: 400;
    letter-spacing: .06em; white-space: nowrap;
    border-bottom: 1px solid currentColor; line-height: 1.15;
  }
  .card--front .brand { left: 28px; top: 70px; gap: 12px; color: var(--brand-green); }
  .card--front .brand-dot { width: 38px; height: 38px; border: 3px solid var(--brand-green); }
  .card--front .brand-name { font-size: 26px; padding-bottom: 4px; }

  .person { position: absolute; left: 34px; top: 150px; color: var(--brand-green); }
  .person-name { font-family: "Noto Sans KR", sans-serif; font-weight: 700; font-size: 20px; letter-spacing: .08em; }
  .person-title { font-family: "Noto Sans KR", sans-serif; font-weight: 400; font-size: 13px; color: var(--text-dark); margin-top: 2px; }

  .contact {
    position: absolute; right: 20px; top: 152px;
    list-style: none; color: var(--text-light); text-align: right;
    font-size: 11px; line-height: 19px; white-space: nowrap;
  }
  .contact li { display: flex; justify-content: flex-end; align-items: flex-start; gap: 7px; }
  .contact .contact-text { display: block; }
  .contact .address { font-family: "Noto Sans KR", sans-serif; font-size: 10px; line-height: 15px; margin-top: 2px; }
  .contact svg { width: 11px; height: 11px; flex: none; margin-top: 4px; }
  .icon-fill { fill: var(--text-light); }
  .icon-line { fill: none; stroke: var(--text-light); stroke-width: 2; }

  .card--back .brand { left: 50%; top: 50%; transform: translate(-50%, -50%); gap: 18px; color: var(--text-light); }
  .card--back .brand-dot { width: 64px; height: 64px; border: 4px solid var(--text-light); }
  .card--back .brand-name { font-size: 46px; padding-bottom: 6px; }
</style>
</head>
<body>
<main class="sheet">
  <section class="card card--front" aria-label="Business card front">
    <svg class="card-art" viewBox="0 0 540 300" preserveAspectRatio="none" aria-hidden="true">
      <path d="M540 14 C420 24 330 60 300 130 C270 200 220 260 110 300 L540 300 Z" fill="var(--brand-green)"/>
      <path d="M540 2 C410 12 318 50 287 122 C257 194 208 252 96 298" fill="none" stroke="var(--brand-green)" stroke-width="4"/>
      <path d="M60 298 C165 286 222 256 250 208" fill="none" stroke="var(--brand-grey)" stroke-width="7" stroke-linecap="round"/>
    </svg>
    <div class="brand">
      <span class="brand-dot"></span>
      <span class="brand-name">ARC VOLLEY</span>
    </div>
    <div class="person">
      <p class="person-name">박 서 윤</p>
      <p class="person-title">대표</p>
    </div>
    <ul class="contact">
      <li><span class="contact-text">010-8472-3916</span>
        <svg viewBox="0 0 24 24" aria-hidden="true"><path class="icon-fill" d="M6.6 10.8a15.2 15.2 0 0 0 6.6 6.6l2.2-2.2c.3-.3.7-.4 1-.2 1.1.4 2.3.6 3.6.6.6 0 1 .4 1 1V20c0 .6-.4 1-1 1C10.6 21 3 13.4 3 4c0-.6.4-1 1-1h3.5c.6 0 1 .4 1 1 0 1.3.2 2.5.6 3.6.1.3 0 .7-.2 1z"/></svg>
      </li>
      <li><span class="contact-text">seoyun.park@arcvolley-example.co.kr</span>
        <svg viewBox="0 0 24 24" aria-hidden="true"><rect class="icon-line" x="2" y="5" width="20" height="14"/><path class="icon-line" d="M2 5l10 8 10-8"/></svg>
      </li>
      <li><span class="contact-text">www.arcvolley-example.co.kr</span>
        <svg viewBox="0 0 24 24" aria-hidden="true"><circle class="icon-line" cx="12" cy="12" r="9"/><path class="icon-line" d="M3 12h18M12 3c3 3 3 15 0 18M12 3c-3 3-3 15 0 18"/></svg>
      </li>
      <li><span class="contact-text">arcvolley</span>
        <svg viewBox="0 0 24 24" aria-hidden="true"><rect class="icon-line" x="4" y="4" width="16" height="16"/></svg>
      </li>
      <li><span class="contact-text address">경기도 용인시 수지구 풍덕천로 456<br>미래타워 5층 501호, 502호</span>
        <svg viewBox="0 0 24 24" aria-hidden="true"><path class="icon-fill" d="M12 2a7 7 0 0 0-7 7c0 5 7 13 7 13s7-8 7-13a7 7 0 0 0-7-7zm0 9.5A2.5 2.5 0 1 1 12 6.5a2.5 2.5 0 0 1 0 5z"/></svg>
      </li>
    </ul>
  </section>

  <section class="card card--back" aria-label="Business card back">
    <div class="brand">
      <span class="brand-dot"></span>
      <span class="brand-name">ARC VOLLEY</span>
    </div>
  </section>
</main>
</body>
</html>
```